Cinder Reef E-Liquid - We need four labels designed and a logo.

We need four labels designed for our eliquid line.
The labels should have some artwork showing the flavors of each of the liquids. The list below shows what they are. Also, we would like some type of logo design, that will keep the labels uniform.
Wobbly Crowns - a cinnamon toast cereal
Orange mango kiwi - Orange, mango, and kiwi.
Pink Tundra - Pink Tundra
Lima Plum - Fiji apple, watermelon, and guava.

Logo Text

Cinder Reef

Requirements
Must have
• The project must have the overlay I just uploaded.

```html
<!DOCTYPE html>
<html lang="en">
<head>
<meta charset="utf-8">
<title>Cinder Reef E-Liquid – Orange Mango Kiwi Label</title>
<link rel="stylesheet" href="https://fonts.googleapis.com/css2?family=Oswald:wght@400;500;600&family=Roboto+Condensed:wght@400;500&family=Montserrat:wght@700&family=Lobster&display=swap">
<style>
  :root {
    --page: #ffffff;
    --red-deep: #5e0b06;
    --red-mid: #a3180c;
    --red-bright: #d8361a;
    --band-dark: rgba(70, 6, 3, 0.55);
    --band-light: rgba(240, 80, 40, 0.35);
    --text-light: #ffffff;
    --text-soft: #e6e6e6;
    --accent-yellow: #f3e316;
    --shield-blue: #1d4fa0;
    --shield-rim: #c9d3e0;
    --gold-light: #fbe6a6;
    --gold-deep: #d99a22;
    --cream: #fff7e2;
  }
  * { box-sizing: border-box; margin: 0; padding: 0; }
  html, body { width: 1200px; height: 774px; overflow: hidden; background: var(--page); }
  .canvas { position: relative; width: 1200px; height: 774px; }

  .label {
    position: absolute; left: 190px; top: 37px; width: 820px; height: 700px; overflow: hidden;
    background:
      linear-gradient(125deg, transparent 0 38%, var(--band-dark) 38% 44%, transparent 44% 100%),
      linear-gradient(125deg, transparent 0 52%, var(--band-light) 52% 55%, transparent 55% 100%),
      linear-gradient(125deg, transparent 0 62%, var(--band-dark) 62% 70%, transparent 70% 100%),
      radial-gradient(ellipse at 45% 40%, var(--red-bright) 0%, var(--red-mid) 45%, var(--red-deep) 100%);
  }

  .warning { position: absolute; left: 29px; top: 30px; width: 138px; color: var(--text-light); font-family: "Roboto Condensed", sans-serif; }
  .warning__title { font-size: 16px; font-weight: 500; margin-bottom: 8px; }
  .warning__body { font-size: 11.4px; line-height: 15.7px; text-transform: uppercase; text-align: justify; }

  .premium-badge {
    position: absolute; left: 32px; top: 282px; width: 127px; height: 66px;
    border: 2px solid var(--text-light); border-radius: 6px;
    display: flex; flex-direction: column; align-items: center; justify-content: center;
    font-family: "Lobster", cursive; color: var(--text-light); line-height: 1;
  }
  .premium-badge__top { font-size: 23px; }
  .premium-badge__bottom { font-size: 20px; }

  .safety-icons { position: absolute; left: 36px; top: 372px; width: 120px; height: 140px; }

  .brand { position: absolute; left: 250px; top: 60px; width: 320px; text-align: center; font-family: "Oswald", sans-serif; font-weight: 600; color: var(--text-light); }
  .brand__ring { width: 44px; height: 44px; margin: 0 auto 8px; border-radius: 50%; background: var(--shield-rim); }
  .brand__name { font-size: 82px; line-height: 0.95; text-transform: none; }

  .tagline { position: absolute; left: 328px; top: 362px; width: 200px; text-align: center; font-family: "Oswald", sans-serif; font-weight: 500; font-style: italic; font-size: 16px; color: var(--text-soft); letter-spacing: 0.5px; }

  .strength { position: absolute; left: 367px; top: 390px; width: 90px; height: 96px; }

  .fruit-art {
    position: absolute; left: 215px; top: 470px; width: 320px; height: 200px; border-radius: 50%;
    background: radial-gradient(ellipse at 55% 45%, #e0323a 0%, #f29a1e 45%, #7dae2c 80%, transparent 100%);
  }
  .liquid-wave { position: absolute; left: 0; top: 520px; width: 820px; height: 180px; }

  .ratio { position: absolute; left: 692px; top: 36px; font-family: "Montserrat", sans-serif; font-weight: 700; font-size: 27px; line-height: 37px; color: var(--text-light); }

  .ingredients {
    position: absolute; left: 690px; top: 118px; width: 100px; height: 242px;
    background: rgba(60, 4, 2, 0.45); padding: 6px;
    writing-mode: vertical-rl; transform: rotate(180deg);
    font-family: "Roboto Condensed", sans-serif; font-size: 14px; line-height: 20px; color: var(--text-light); text-align: justify;
  }
  .ingredients__title { font-size: 17px; letter-spacing: 0.5px; }
  .ingredients__flavours { color: var(--accent-yellow); }

  .age-notice { position: absolute; left: 693px; top: 375px; font-family: "Oswald", sans-serif; color: var(--text-light); line-height: 1.05; }
  .age-notice__main { font-size: 21px; font-weight: 600; }
  .age-notice__sub { font-size: 17px; font-weight: 400; }
  .age-notice__last { font-size: 23px; font-weight: 500; }
</style>
</head>
<body>
<main class="canvas">
  <section class="label" aria-label="Cinder Reef Orange Mango Kiwi label">

    <div class="liquid-wave" role="img" aria-label="Golden e-liquid wave with bubbles">
      <svg width="820" height="180" viewBox="0 0 820 180" aria-hidden="true">
        <defs>
          <linearGradient id="waveGold" x1="0" y1="0" x2="0" y2="1">
            <stop offset="0" stop-color="var(--cream)"/>
            <stop offset="0.35" stop-color="var(--gold-light)"/>
            <stop offset="1" stop-color="var(--gold-deep)"/>
          </linearGradient>
        </defs>
        <path d="M0 10 C150 70 300 60 450 80 C600 100 720 40 820 30 L820 180 L0 180 Z" fill="url(#waveGold)"/>
      </svg>
    </div>

    <div class="fruit-art" role="img" aria-label="Illustration of kiwi, mango and orange with a splash of liquid"></div>

    <div class="warning">
      <p class="warning__title">WARNING:</p>
      <p class="warning__body">E-liquid contains nicotine which is both highly toxic and very addictive. Keep well away from children and pets. E-liquid is only intended to be used with your electronic cigarettes, e-cigs, e-cigars, e-pipes or vaporizers. Not for sale to anyone under the age of 18.</p>
    </div>

    <div class="premium-badge">
      <span class="premium-badge__top">Premium</span>
      <span class="premium-badge__bottom">Vape liquid</span>
    </div>

    <svg class="safety-icons" viewBox="0 0 120 140" aria-label="Safety icons">
      <g fill="#fff" stroke="#c0160c" stroke-width="3">
        <circle cx="18" cy="18" r="16"/>
        <circle cx="82" cy="18" r="16"/>
        <circle cx="18" cy="110" r="16"/>
        <circle cx="82" cy="110" r="16"/>
      </g>
      <path d="M10 18 a8 8 0 0 1 14 -5 M26 18 a8 8 0 0 1 -14 5" fill="none" stroke="#222" stroke-width="2.5"/>
      <text x="82" y="24" text-anchor="middle" font-family="Oswald, sans-serif" font-weight="600" font-size="16" fill="#222">21</text>
      <rect x="52" y="52" width="24" height="24" transform="rotate(45 64 64)" fill="#fff" stroke="#c0160c" stroke-width="3"/>
      <text x="64" y="71" text-anchor="middle" font-family="Oswald, sans-serif" font-weight="600" font-size="16" fill="#c0160c">!</text>
      <line x1="7" y1="99" x2="29" y2="121" stroke="#c0160c" stroke-width="3"/>
      <rect x="76" y="106" width="12" height="12" fill="#222"/>
      <rect x="74" y="102" width="16" height="3" fill="#222"/>
    </svg>

    <div class="brand">
      <div class="brand__ring"></div>
      <p class="brand__name">Cinder<br>Reef</p>
    </div>

    <p class="tagline">PREMIUM E LIQUID</p>

    <svg class="strength" viewBox="0 0 90 96" aria-label="3 mg nicotine strength">
      <path d="M45 3 L85 14 L80 60 Q70 82 45 93 Q20 82 10 60 L5 14 Z" fill="var(--shield-blue)" stroke="var(--shield-rim)" stroke-width="5"/>
      <text x="45" y="58" text-anchor="middle" font-family="Oswald, sans-serif" font-weight="600" font-size="42" fill="#fff">3</text>
      <text x="45" y="78" text-anchor="middle" font-family="Oswald, sans-serif" font-weight="500" font-size="16" fill="#fff">MG</text>
    </svg>

    <div class="ratio">
      <p>VG: 70</p>
      <p>PG: 30</p>
    </div>

    <p class="ingredients"><span class="ingredients__title">INGREDIENTS:</span>Propylene Glycol (PG), Vegetable Glycerine (VG), Water, Flavorings – <span class="ingredients__flavours">Mango, Kiwi, Orange.</span></p>

    <div class="age-notice">
      <p class="age-notice__main">21 AND OVER</p>
      <p class="age-notice__sub">UNDER AGE SALE</p>
      <p class="age-notice__last">PROHIBITED</p>
    </div>
  </section>
</main>
</body>
</html>
```